Creative, fresh business card design for Brindlecrest Linings

We need a fresh, creative business card design for Brindlecrest Linings. We are the manufacturer of Brindlecrest Linings in Australia. Wall panels are 2400 x 1200mm panels made from MDF and feature 3D patterns on the face of the panel. The colours to be used are green, silver/grey and white RGB
Red 187
Green 207
Blue 65.

An idea is to possibly use a watermark of one of our designs as a background (like on the "Lattice" design on the left hand side of page 2 of our brochure).

Target Market(s)

Interior designers, architects, builders and home renovators

Industry/Entity Type

Business

Contact Information for Business Card

Details to go on the card are:
Our logo (attached),
Slogan: "Decorative panels for interiors and exteriors",
Contact name,
Position,
Mobile phone number,
Business address,
Business phone,
Business fax,
Website and
Email address.

I have attached a few images of our panels and our brochure for reference.

The colours of the business card should feature our logo colours which are: RGB
Red 187
Green 207
Blue 65

Requirements
Must have
• Very modern fonts and design. Some of the designs shown especially the "Weave" design which is a popular design.
Nice to have
• Creative but simple design. Very contemporary.
Should not have
• Anything ornate or old fashioned.

```html
<!DOCTYPE html>
<html lang="en">
<head>
<meta charset="utf-8">
<title>Brindlecrest Linings – Business Card</title>
<link rel="stylesheet" href="https://fonts.googleapis.com/css2?family=Questrial&display=swap">
<style>
  :root {
    --brand-green: rgb(187, 207, 65);
    --card-black: #141414;
    --card-black-deep: #0b0b0b;
    --text-grey: #a8a8a8;
    --silver: #b9b9b9;
    --page-bg: #e4e4e2;
    --faint: rgba(255, 255, 255, 0.06);
  }
  * { box-sizing: border-box; margin: 0; padding: 0; }
  html, body {
    width: 1200px;
    height: 1022px;
    overflow: hidden;
    background: var(--page-bg);
    font-family: "Questrial", "Century Gothic", sans-serif;
  }
  .sheet {
    position: relative;
    width: 1200px;
    height: 1022px;
    display: flex;
    flex-direction: column;
    align-items: center;
    justify-content: center;
    gap: 22px;
  }
  .card {
    position: relative;
    width: 840px;
    height: 480px;
    background: var(--card-black);
    overflow: hidden;
    box-shadow: 0 6px 18px rgba(0, 0, 0, 0.25);
  }
  .card__texture {
    position: absolute;
    inset: 0;
    background: radial-gradient(ellipse at 40% 30%, #1f1f1f 0%, var(--card-black) 55%, var(--card-black-deep) 100%);
  }
  .card__band {
    position: absolute;
    top: 0;
    bottom: 0;
    width: 110px;
    background: var(--brand-green);
  }
  .card--front .card__band { left: 0; }
  .card--back .card__band { right: 0; }

  .card__mark-faint {
    position: absolute;
    width: 230px;
    height: 230px;
    background: var(--faint);
  }
  .card--front .card__mark-faint { right: 70px; bottom: 60px; }
  .card--back .card__mark-faint { left: 60px; bottom: -60px; }

  .brand {
    position: absolute;
    display: flex;
    align-items: center;
    gap: 16px;
  }
  .brand__square {
    width: 58px;
    height: 58px;
    background: var(--brand-green);
    flex: none;
  }
  .brand__text { display: flex; flex-direction: column; gap: 6px; }
  .brand__name {
    color: var(--brand-green);
    font-size: 28px;
    letter-spacing: 0.5px;
    white-space: nowrap;
  }
  .brand__slogan {
    color: var(--text-grey);
    font-size: 14px;
    letter-spacing: 1.5px;
    line-height: 1.3;
  }
  .card--front .brand { top: 40px; right: 40px; }
  .card--back .brand { top: 50%; left: 140px; transform: translateY(-50%); }
  .card--back .brand__square { width: 84px; height: 84px; }
  .card--back .brand__name { font-size: 40px; }
  .card--back .brand__slogan { font-size: 17px; }

  .person {
    position: absolute;
    left: 150px;
    top: 150px;
  }
  .person__name {
    color: var(--brand-green);
    font-size: 38px;
    letter-spacing: 0.5px;
  }
  .person__role {
    color: var(--text-grey);
    font-size: 20px;
    letter-spacing: 1px;
    margin-top: 4px;
  }

  .contacts {
    position: absolute;
    left: 150px;
    top: 252px;
    list-style: none;
    display: flex;
    flex-direction: column;
    gap: 6px;
  }
  .contacts__item {
    display: flex;
    align-items: center;
    gap: 14px;
    color: var(--text-grey);
    font-size: 21px;
    letter-spacing: 1.5px;
  }
  .contacts__icon {
    width: 20px;
    height: 20px;
    flex: none;
    fill: var(--brand-green);
  }

  .address {
    position: absolute;
    left: 470px;
    top: 300px;
    color: var(--text-grey);
    font-size: 21px;
    font-style: normal;
    letter-spacing: 1.5px;
    line-height: 1.4;
  }
</style>
</head>
<body>
<main class="sheet">

  <section class="card card--front" aria-label="Business card, contact side">
    <div class="card__texture" role="img" aria-label="Subtle embossed circular wall-panel pattern on black"></div>
    <div class="card__mark-faint" aria-hidden="true"></div>
    <div class="card__band" aria-hidden="true"></div>

    <div class="brand">
      <span class="brand__square" aria-hidden="true"></span>
      <div class="brand__text">
        <span class="brand__name">Brindlecrest Linings</span>
        <span class="brand__slogan">decorative panels for<br>interiors &amp; landscapes</span>
      </div>
    </div>

    <div class="person">
      <h1 class="person__name">Owen Hartley</h1>
      <p class="person__role">President</p>
    </div>

    <ul class="contacts">
      <li class="contacts__item">
        <svg class="contacts__icon" viewBox="0 0 20 20" aria-hidden="true"><path d="M6 1h8a1 1 0 0 1 1 1v16a1 1 0 0 1-1 1H6a1 1 0 0 1-1-1V2a1 1 0 0 1 1-1zm1 2v12h6V3zm3 13.2a1 1 0 1 0 0 2 1 1 0 0 0 0-2z"/></svg>
        310. 555. 0142
      </li>
      <li class="contacts__item">
        <svg class="contacts__icon" viewBox="0 0 20 20" aria-hidden="true"><path d="M4.5 2l3 .5 1.2 3.8-2 1.4a11 11 0 0 0 5.6 5.6l1.4-2 3.8 1.2.5 3-2 2C8.5 17.5 2.5 11.5 2.5 4z"/></svg>
        310. 555. 0187
      </li>
      <li class="contacts__item">
        <svg class="contacts__icon" viewBox="0 0 20 20" aria-hidden="true"><path d="M5 1h8l2 2v4H5zm-3 7h16a1 1 0 0 1 1 1v6h-3v4H4v-4H1V9a1 1 0 0 1 1-1zm4 6v3h8v-3z"/></svg>
        310. 555. 0193
      </li>
      <li class="contacts__item">
        <svg class="contacts__icon" viewBox="0 0 20 20" aria-hidden="true"><path d="M1 4h18v12H1zm2 2v.3l7 5 7-5V6zm0 2.7V14h14V8.7l-7 5z"/></svg>
        owen@brindlecrest.com
      </li>
      <li class="contacts__item">
        <svg class="contacts__icon" viewBox="0 0 20 20" aria-hidden="true"><path d="M10 1a9 9 0 1 0 0 18 9 9 0 0 0 0-18zm0 2c.9 0 2 1.8 2.4 4.5H7.6C8 4.8 9.1 3 10 3zM5.6 7.5H3.4a7 7 0 0 1 3.5-3.8 11 11 0 0 0-1.3 3.8zm0 5a11 11 0 0 0 1.3 3.8 7 7 0 0 1-3.5-3.8zm2 0h4.8C12 15.2 10.9 17 10 17s-2-1.8-2.4-4.5zm6.8 0h2.2a7 7 0 0 1-3.5 3.8 11 11 0 0 0 1.3-3.8zm0-5a11 11 0 0 0-1.3-3.8 7 7 0 0 1 3.5 3.8zM3.1 9.5h2.4v1H3.1zm4.4 0h5v1h-5zm7 0h2.4v1h-2.4z"/></svg>
        www.brindlecrest.com
      </li>
    </ul>

    <address class="address">4120 Harbor Lane<br>Westmere, CA 90418</address>
  </section>

  <section class="card card--back" aria-label="Business card, brand side">
    <div class="card__texture" role="img" aria-label="Subtle embossed circular wall-panel pattern on black"></div>
    <div class="card__mark-faint" aria-hidden="true"></div>
    <div class="card__band" aria-hidden="true"></div>

    <div class="brand">
      <span class="brand__square" aria-hidden="true"></span>
      <div class="brand__text">
        <span class="brand__name">Brindlecrest Linings</span>
        <span class="brand__slogan">decorative panels for interiors &amp; landscapes</span>
      </div>
    </div>
  </section>

</main>
</body>
</html>
```